KLT, Inc. business card desing

Design a business card for an contemporary e commerce company that sells fragrances and cosmetics. State of the art , high tech and super very fast delivery

Target Market(s)

e commerce customers like Bramble, Tolvex , and retailers wesites

Industry/Entity Type

Business

Contact Information for Business Card

On the Front :

scentharborline.example with some design element

On the back :
Dr. Marek Thornby
President

Phone ( icom) 555.207.6431
Cell (icon) 555.284.9062
Fax(icon) 555.613.4870
email (icon) marek@scentharborline.example

4815 Cedar Lane
Linwood Harbor, NY 11990

Colors
b768aa
e667a6
abd036

Requirements
Must have
• all the above content info
Nice to have
• Could have and abstract perfume bottle
Should not have
• no faces, facial features,

```html
<!DOCTYPE html>
<html lang="en">
<head>
<meta charset="utf-8">
<title>scentharborline.example business card</title>
<link href="https://fonts.googleapis.com/css2?family=Open+Sans:wght@400;600;700&display=swap" rel="stylesheet">
<style>
  :root {
    --backdrop: #47365f;
    --card-pink: #fcbdf6;
    --card-white: #ffffff;
    --magenta: #e667a6;
    --orchid: #b768aa;
    --deep-purple: #5b2a8c;
    --bottle-tint: #f0a5e4;
    --bottle-tint-light: #f7cfee;
  }
  * { box-sizing: border-box; margin: 0; padding: 0; }
  html, body {
    width: 1200px; height: 876px; overflow: hidden;
    background: var(--backdrop);
    font-family: "Open Sans", Arial, sans-serif;
  }
  .canvas { position: relative; width: 1200px; height: 876px; }

  .card {
    position: absolute;
    width: 560px; height: 320px;
    overflow: hidden;
    box-shadow: 0 12px 30px rgba(0,0,0,.35);
  }
  .card-front { left: 80px; top: 100px; background: var(--card-pink); }
  .card-back  { left: 560px; top: 450px; background: var(--card-white); }

  .swoosh { position: absolute; left: 0; top: 0; width: 100%; height: 100%; }

  .bottle-area {
    position: absolute;
    border-radius: 46% 46% 30% 30%;
  }
  .card-front .bottle-area {
    left: 220px; top: 50px; width: 110px; height: 160px;
    background: var(--bottle-tint);
  }
  .card-back .bottle-area {
    left: 92px; top: 112px; width: 80px; height: 120px;
    background: var(--bottle-tint-light);
  }

  .site-url {
    position: absolute; left: 0; right: 0; top: 122px;
    text-align: center;
    font-size: 24px; font-weight: 600;
    color: var(--deep-purple);
  }

  .identity { position: absolute; left: 28px; top: 42px; }
  .person-name {
    color: var(--deep-purple);
    font-weight: 700; font-size: 26px; letter-spacing: .5px;
    line-height: 1;
  }
  .person-name .title-prefix { font-size: 18px; margin-right: 4px; }
  .person-role {
    margin-top: 4px; margin-left: 40px;
    color: var(--orchid);
    font-size: 14px; font-weight: 600; letter-spacing: 3px;
  }

  .contact-list {
    position: absolute; right: 26px; top: 54px;
    list-style: none; text-align: right;
    color: var(--deep-purple);
    font-size: 13px; line-height: 19px;
  }
  .contact-list li { display: flex; justify-content: flex-end; align-items: center; gap: 7px; white-space: nowrap; }
  .contact-list .gap-before { margin-top: 12px; }
  .contact-list svg { width: 11px; height: 11px; fill: var(--deep-purple); flex: none; }
</style>
</head>
<body>
<main class="canvas">

  <section class="card card-front" aria-label="Card front">
    <div class="bottle-area" role="img" aria-label="Abstract perfume bottle silhouette"></div>
    <p class="site-url">scentharborline.example</p>
    <svg class="swoosh" viewBox="0 0 560 320" preserveAspectRatio="none" aria-hidden="true">
      <path d="M0,320 L0,300 C170,262 370,236 560,172 L560,320 Z" fill="var(--magenta)"/>
      <path d="M0,292 C170,252 370,226 560,160 L560,168 C370,234 170,262 0,298 Z" fill="var(--deep-purple)"/>
      <path d="M0,282 C170,244 370,216 560,148 L560,155 C370,222 170,250 0,287 Z" fill="var(--magenta)"/>
    </svg>
  </section>

  <section class="card card-back" aria-label="Card back">
    <div class="bottle-area" role="img" aria-label="Abstract perfume bottle silhouette"></div>
    <div class="identity">
      <h1 class="person-name"><span class="title-prefix">Dr.</span>MAREK THORNBY</h1>
      <p class="person-role">PRESIDENT</p>
    </div>
    <ul class="contact-list">
      <li>555.284.9062
        <svg viewBox="0 0 12 12" aria-label="Cell"><path d="M3 0h6a1 1 0 0 1 1 1v10a1 1 0 0 1-1 1H3a1 1 0 0 1-1-1V1a1 1 0 0 1 1-1zm0 1.5v8h6v-8z"/></svg></li>
      <li>555.207.6431
        <svg viewBox="0 0 12 12" aria-label="Phone"><path d="M1 3c0-1 1-2 5-2s5 1 5 2v1H8V3H4v1H1zM3 5h6l2 3v3H1V8z"/></svg></li>
      <li>555.613.4870
        <svg viewBox="0 0 12 12" aria-label="Fax"><path d="M3 0h6v4H3zM1 5h10v6H1zm2 2v1h2V7z"/></svg></li>
      <li class="gap-before">marek@scentharborline.example
        <svg viewBox="0 0 12 12" aria-label="Email"><path d="M0 2h12v8H0zm1 1v.4l5 3.4 5-3.4V3z"/></svg></li>
      <li>4815 Cedar Lane, Linwood Harbor, NY 11990
        <svg viewBox="0 0 12 12" aria-label="Address"><path d="M6 0a4 4 0 0 1 4 4c0 3-4 8-4 8S2 7 2 4a4 4 0 0 1 4-4zm0 2.5A1.5 1.5 0 1 0 6 5.5 1.5 1.5 0 0 0 6 2.5z"/></svg></li>
    </ul>
    <svg class="swoosh" viewBox="0 0 560 320" preserveAspectRatio="none" aria-hidden="true">
      <path d="M0,320 L0,302 C160,270 380,248 560,214 L560,320 Z" fill="var(--magenta)"/>
      <path d="M0,294 C160,262 380,238 560,202 L560,210 C380,246 160,270 0,299 Z" fill="var(--deep-purple)"/>
      <path d="M230,250 C350,230 460,212 560,190 L560,198 C460,220 350,238 230,254 Z" fill="var(--magenta)"/>
    </svg>
  </section>

</main>
</body>
</html>
```